Designer needed for Fitness Product Enhanced Brand Content

We are looking for an experienced graphic designer and photo editor to create stunning, eye catching A+ content for our products sold on Brindle Market. A+ content integrates detailed product descriptions, rich images, and comparison charts to help customers make informed buying decisions (See attached A+ EBC example).

A+ Content also includes minimal text so experience with marketing copy is a plus!

Please see the attached Zorel-Bondix image for reference. The designer should be able to create a similar image using the attached PNG files.

This specific project is for Zorel Tempest which is a pre-workout supplement. To learn more about the product please go to our website:
https://zorelworks.com/tempest-pre-workout.html

Attached are all angles of the product.

We are looking forward to working with you!

Industry/Entity Type

Fitness

Colors

Designer to choose colors to be used in the design.

Requirements
Must have
• The layout should include a combination of the following images.
• Dimensions:
• Large Image: 1800 x 540
• Small Image: 900 x 900

```html
<!DOCTYPE html>
<html lang="en">
<head>
<meta charset="utf-8">
<title>Zorel Pre-Workout Supplement – Brand Content</title>
<link rel="stylesheet" href="https://fonts.googleapis.com/css2?family=Exo+2:ital,wght@0,300;0,700;1,300;1,600;1,800&family=Lato:wght@400;700;900&display=swap">
<style>
  :root {
    --backdrop: #000000;
    --page: #fcfcfc;
    --ink: #111111;
    --dark: #0e0e10;
    --dark-2: #1c1c20;
    --yellow: #f4e21a;
    --gold: #f1b415;
    --gold-deep: #e59c10;
    --photo-1: #2b3036;
    --photo-2: #5b636b;
    --tub-blue: #1f3b8c;
  }
  * { box-sizing: border-box; margin: 0; padding: 0; }
  html, body { width: 1200px; height: 1200px; overflow: hidden; background: var(--backdrop); }
  body { position: relative; font-family: "Lato", sans-serif; color: var(--ink); }

  .sheet { position: absolute; left: 259px; top: 53px; width: 682px; height: 1095px; background: var(--page); }

  /* hero banner */
  .hero { position: absolute; left: 14px; top: 12px; width: 649px; height: 202px; background: linear-gradient(90deg, var(--dark) 0%, var(--dark-2) 55%, var(--dark) 100%); overflow: hidden; }
  .hero-photo { position: absolute; left: 345px; top: 0; width: 304px; height: 202px; background: radial-gradient(ellipse at 70% 55%, var(--photo-2), var(--photo-1) 70%, var(--dark) 100%); }
  .hero-tub { position: absolute; left: 434px; top: 86px; width: 72px; height: 108px; border-radius: 6px; background: linear-gradient(135deg, var(--tub-blue), var(--yellow) 55%, var(--tub-blue)); }
  .hero-headline { position: absolute; left: 23px; top: 32px; font-family: "Exo 2", sans-serif; font-style: italic; font-weight: 300; font-size: 30px; line-height: 28.5px; letter-spacing: 3px; color: var(--yellow); text-transform: uppercase; }
  .hero-headline strong { font-weight: 800; color: var(--gold); }
  .spec-tags { position: absolute; right: 0; top: 24px; list-style: none; }
  .spec-tags li { width: 120px; height: 14px; margin-bottom: 5.5px; background: var(--yellow); clip-path: polygon(8% 0, 100% 0, 100% 100%, 0 100%); font-family: "Exo 2", sans-serif; font-style: italic; font-weight: 700; font-size: 8px; line-height: 14px; padding-left: 17px; color: var(--ink); }

  /* intro */
  .intro-tub { position: absolute; left: 73px; top: 255px; width: 108px; height: 163px; border-radius: 8px; background: linear-gradient(150deg, var(--tub-blue) 0%, var(--yellow) 40%, var(--tub-blue) 70%, var(--yellow) 100%); }
  .intro-shadow { position: absolute; left: 12px; top: 402px; width: 230px; height: 22px; border-radius: 50%; background: radial-gradient(ellipse, rgba(0,0,0,.35), rgba(0,0,0,0) 70%); }
  .intro-title { position: absolute; left: 259px; top: 258px; font-family: "Exo 2", sans-serif; font-style: italic; font-weight: 800; font-size: 26px; line-height: 29px; letter-spacing: 1.5px; color: var(--gold); text-transform: uppercase; }
  .intro-text { position: absolute; left: 263px; top: 327px; width: 360px; font-size: 14.5px; line-height: 19px; letter-spacing: 1px; }

  /* ingredients */
  .ingredient { position: absolute; left: 10px; width: 630px; }
  .ingredient-tag { height: 20px; width: 230px; background: linear-gradient(90deg, rgba(244,226,26,0) 0%, var(--yellow) 55%, var(--gold) 100%); clip-path: polygon(0 0, 100% 0, 94% 100%, 0 100%); font-style: italic; font-weight: 900; font-size: 11.5px; line-height: 20px; letter-spacing: .8px; text-align: right; padding-right: 22px; }
  .ingredient p { margin: 13px 0 0 62px; font-size: 10.5px; line-height: 14px; letter-spacing: .9px; }

  /* benefits */
  .benefit-band { position: absolute; left: 43px; top: 732px; width: 593px; height: 33px; background: linear-gradient(90deg, var(--gold) 0%, var(--yellow) 60%, var(--yellow) 100%); display: flex; }
  .benefit-band span { font-family: "Exo 2", sans-serif; font-style: italic; font-weight: 800; font-size: 23px; line-height: 33px; letter-spacing: 1.5px; color: var(--page); text-shadow: 1px 1px 0 rgba(0,0,0,.35); }
  .benefit-text { position: absolute; width: 168px; font-weight: 900; font-size: 10px; line-height: 12px; letter-spacing: .6px; }

  /* footer banner */
  .footer-banner { position: absolute; left: 15px; top: 939px; width: 651px; height: 134px; background: linear-gradient(90deg, var(--dark) 0%, var(--dark-2) 60%, var(--dark) 100%); overflow: hidden; }
  .footer-glow { position: absolute; left: 60px; top: 10px; width: 150px; height: 120px; background: radial-gradient(ellipse, rgba(244,226,26,.35), rgba(0,0,0,0) 70%); }
  .footer-shaker { position: absolute; left: 78px; top: 13px; width: 44px; height: 110px; border-radius: 5px; background: linear-gradient(90deg, var(--gold-deep), var(--yellow)); }
  .footer-tub { position: absolute; left: 112px; top: 18px; width: 72px; height: 108px; border-radius: 6px; background: linear-gradient(140deg, var(--tub-blue), var(--yellow) 50%, var(--tub-blue)); }
  .brand-name { position: absolute; left: 415px; top: 44px; display: flex; align-items: center; gap: 12px; font-weight: 900; font-size: 48px; color: var(--yellow); }
  .brand-name i { width: 22px; height: 22px; background: var(--yellow); display: block; }
</style>
</head>
<body>
  <main class="sheet">
    <section class="hero">
      <div class="hero-photo" role="img" aria-label="Gym scene with athletes and a weight plate"></div>
      <div class="hero-tub" role="img" aria-label="Zorel Tempest pre-workout tub"></div>
      <h1 class="hero-headline">Boost your<br>performance<br>to the<br><strong>maximum</strong><br>level.</h1>
      <ul class="spec-tags">
        <li>200mg Caffeine</li>
        <li>4G L-Citruline</li>
        <li>1.5 G Taurine</li>
        <li>185mg Alpha GPC</li>
      </ul>
    </section>

    <div class="intro-shadow"></div>
    <div class="intro-tub" role="img" aria-label="Zorel Tempest pre-workout tub product shot"></div>
    <h2 class="intro-title">Zorel Pre-Workout<br>Supplement</h2>
    <p class="intro-text">Contains all the necessary ingredients to help you increase stamina, last longer and boost your performance during your intense workouts.</p>

    <section class="ingredient" style="top:456px">
      <div class="ingredient-tag">Caffeine Anhydrous</div>
      <p>This powdered version of caffeine boosts dopamine and serotonin levels which results in more energy. more alertness and less fatigue without the crash.</p>
    </section>
    <section class="ingredient" style="top:525px">
      <div class="ingredient-tag">L-Citruline</div>
      <p>Found Naturally in watermelons, L-Citruline is an Amino Acid that strenthens muscles, improves heart and increast blood flow.</p>
    </section>
    <section class="ingredient" style="top:591px">
      <div class="ingredient-tag">Taurine</div>
      <p>Helps you get closer to your goal by heping the body metabolize fats and curbing hunger. Taurine calms down an exited nervous system thus allowing for a more effecient workout.</p>
    </section>
    <section class="ingredient" style="top:656px">
      <div class="ingredient-tag">Alpha GPC</div>
      <p style="margin-top:16px">Aplha GPC is a cognitive enhancer known for its ability to improve memory. improve your overall brain health by encouraging the development of new brain cells.</p>
    </section>

    <div class="benefit-band">
      <span style="margin-left:27px">ENERGY</span>
      <span style="margin-left:104px">PUMP</span>
      <span style="margin-left:125px">FOCUS</span>
    </div>
    <p class="benefit-text" style="left:70px;top:779px">Power trough your workouts with a much-needed energy boost. Caffeine helps to increase dopamine and serotonin levels so you can work out even longer. Taurine curbs your hunger and calms down an overly-exited nevous system once you finish your workout remime.</p>
    <p class="benefit-text" style="left:260px;top:781px">improve the quality of your workout by increasing blood flow and simukating cintinued muscle growth. The pump gives you and extra boost of confidence mentally and physically and allows you to finish your workout feeling better than when you started.</p>
    <p class="benefit-text" style="left:461px;top:785px">Spend less time fighting yourself at the gym and more time focusing on what matters the most. Alpha GPC plays the connection between brain and body so you can focus on the highlights of your workout.</p>

    <section class="footer-banner">
      <div class="footer-glow"></div>
      <div class="footer-shaker" role="img" aria-label="Yellow shaker bottle"></div>
      <div class="footer-tub" role="img" aria-label="Zorel Tempest pre-workout tub"></div>
      <div class="brand-name"><i></i>Zorel</div>
    </section>
  </main>
</body>
</html>
```